Brightway Haul & Repair Services, are a company that offers a 'one stop shop' pre-move clean up a

I have already selected a logo which I would like on the front of the business cards along with phone numbers, web address and email which are:
0419574302
www.brightwayhaul.com.au
brightwayhaulrepair@mailbox.example

On the back of the card I would like to list some of the types of service we offer (clean - move - repairs/maintenance) which are:
CLEAN - windows, gutters, solar panels, driveways/paths, carpets.
MOVE - Small/medium size house/office moves, large item pick-up & delivery, yard clean-up and removal.
General maintenance and repairs.

I would like the blue logo on a gray background.

Thanks

```html
<!DOCTYPE html>
<html lang="en">
<head>
<meta charset="utf-8">
<title>Brightway Haul &amp; Repair Services – Business Card</title>
<link rel="stylesheet" href="https://fonts.googleapis.com/css2?family=Exo+2:wght@400;700&display=swap">
<style>
  :root {
    --brand-blue: #1565ae;
    --card-grey: #dcdddf;
    --card-white: #ffffff;
    --stage: #2b2b2d;
    --text-white: #ffffff;
  }
  * { box-sizing: border-box; margin: 0; padding: 0; }
  html, body {
    width: 1200px; height: 900px; overflow: hidden;
    background: var(--stage);
    font-family: "Exo 2", Arial, sans-serif;
  }
  .stage { position: relative; width: 1200px; height: 900px; }
  .card {
    position: absolute; top: 308px;
    width: 513px; height: 284px;
    border-radius: 17px; overflow: hidden;
  }
  .card-front { left: 73px; background: var(--card-grey); }
  .card-back { left: 615px; background: var(--card-white); }
  .card-band {
    position: absolute; left: 0; right: 0; top: 181px; bottom: 0;
    background: var(--brand-blue);
  }
  .brand-name {
    position: absolute; color: var(--brand-blue);
    font-weight: 700; text-transform: uppercase; line-height: 1.05;
  }
  .card-front .brand-name {
    right: 28px; top: 58px; width: 300px; text-align: right;
    font-size: 30px;
  }
  .card-front .brand-name .brand-sub { display: block; font-size: 17px; margin-top: 6px; }
  .contact-list {
    position: absolute; right: 28px; top: 196px;
    list-style: none; text-align: right;
    color: var(--text-white); font-size: 14px; line-height: 21px;
  }
  .contact-list li { display: flex; justify-content: flex-end; align-items: center; gap: 4px; }
  .contact-list svg { width: 11px; height: 11px; }
  .service-list {
    position: absolute; left: 29px; top: 28px; width: 320px;
    color: var(--brand-blue); font-size: 15px; line-height: 20px;
  }
  .service-list p { margin-bottom: 9px; }
  .card-back .brand-name {
    left: 29px; top: 229px; color: var(--text-white);
    font-size: 15px;
  }
  .card-back .brand-name .brand-sub { display: block; font-size: 9px; margin-top: 2px; }
</style>
</head>
<body>
<main class="stage">
  <section class="card card-front" aria-label="Card front">
    <div class="card-band"></div>
    <h1 class="brand-name">Brightway Haul <span class="brand-sub">&amp; Repair Services</span></h1>
    <ul class="contact-list">
      <li>0419 574 302
        <svg viewBox="0 0 12 12" aria-hidden="true"><path d="M3 1l2 2-1 1.5c.6 1.4 1.6 2.4 3 3L8.5 6.5l2 2L9 10.5C5 10 2 7 1.5 3z" fill="none" stroke="#fff" stroke-width="1"/></svg>
      </li>
      <li>www.brightwayhaul.com.au
        <svg viewBox="0 0 12 12" aria-hidden="true"><circle cx="6" cy="6" r="5" fill="none" stroke="#fff"/><ellipse cx="6" cy="6" rx="2.2" ry="5" fill="none" stroke="#fff"/><path d="M1 6h10" stroke="#fff"/></svg>
      </li>
      <li>brightwayhaulrepair@mailbox.example
        <svg viewBox="0 0 12 12" aria-hidden="true"><rect x="1" y="3" width="10" height="7" fill="#fff"/><path d="M1 3l5 4 5-4" fill="none" stroke="#1565ae"/></svg>
      </li>
    </ul>
  </section>

  <section class="card card-back" aria-label="Card back">
    <div class="card-band"></div>
    <div class="service-list">
      <p>CLEAN - windows, gutters, solar panels, driveways/paths, carpets.</p>
      <p>MOVE - Small/medium size house/office moves, large item pick-up &amp; delivery, yard clean-up and removal.</p>
      <p>General maintenance and repairs.</p>
    </div>
    <h2 class="brand-name">Brightway Haul <span class="brand-sub">&amp; Repair Services</span></h2>
  </section>
</main>
</body>
</html>
```